New emergency medical service needs a marketing flyer for prospective customers

We need a tri fold brochure on an 8.5 X 11 stock for a new emergency medical service in Pennsylvania. We provide basic first aid and now Covid-19 pre screening and temperature monitoring for special events, large gatherings and businesses. Examples of these would be but not limited to: Sporting events, carnivals, festivals, craft shows, warehouses, churches, manufacturing facilities, industrial buildings, large construction sites, multi occupancy officer buildings. The market for this is pretty much untouched and endless. we would like to use gray as the back ground color and obviously our logo. The final design should grab their attention and communicate the importance of having trained and certified professionals at their event or facility. We want to give them that piece of mind they are in good hands with us.

Target Market(s)

primary focus is going to be on businesses with large offices, large buildings or lots of foot traffic in and out of the building

Requirements
Must have
• gray background, pictures, company phone # , company web site, and contact email address. I will provide all that information to the winner to add at the end.
Nice to have
• pictures that covers the whole front cover with logo at top

```html
<!DOCTYPE html>
<html lang="en">
<head>
<meta charset="utf-8">
<title>Covid-19 Pre Screening and Temperature Monitoring – Tri-fold Brochure</title>
<link rel="stylesheet" href="https://fonts.googleapis.com/css2?family=Arimo:wght@400;700&display=swap">
<style>
  :root {
    --ink: #231f20;
    --white: #ffffff;
    --gray-light: #c8c8c9;
    --gray-mid: #a9a9ab;
    --gray-dark: #7e7e81;
    --band-black: #231f20;
  }
  * { margin: 0; padding: 0; box-sizing: border-box; }
  html, body { width: 1200px; height: 927px; overflow: hidden; background: var(--white); }
  body { font-family: "Arimo", Arial, sans-serif; color: var(--ink); }

  .brochure { position: relative; width: 1200px; height: 927px; overflow: hidden; background: var(--white); }
  .backdrop { position: absolute; inset: 0; width: 1200px; height: 927px; }

  .panel { position: absolute; top: 0; height: 927px; width: 400px; }
  .panel--about { left: 0; }
  .panel--services { left: 400px; color: var(--white); }
  .panel--team { left: 800px; }

  /* Left panel */
  .cover-title { position: absolute; top: 78px; left: 0; width: 400px; text-align: center; }
  .cover-title__main { font-size: 54px; font-weight: 700; line-height: 1.1; }
  .cover-title__sub { font-size: 32px; line-height: 40px; margin-top: 2px; }

  .section-heading { font-size: 27px; font-weight: 700; line-height: 1.2; }

  .about { position: absolute; top: 441px; left: 40px; width: 328px; }
  .body-copy { font-size: 14.6px; line-height: 21.3px; text-align: justify; margin-top: 14px; }

  .dots { position: absolute; top: 796px; left: 44px; display: flex; gap: 36px; }
  .dot { width: 78px; height: 80px; }

  /* Middle panel */
  .services-tagline { position: absolute; top: 50px; left: 0; width: 400px; text-align: center;
    font-size: 28px; font-weight: 700; line-height: 36px; }
  .services { position: absolute; top: 185px; left: 37px; width: 328px; }
  .services .section-heading { color: var(--white); }
  .services .body-copy { line-height: 24.2px; margin-top: 14px; }
  .services .body-copy + .body-copy { margin-top: 30px; }

  /* Right panel */
  .team { position: absolute; top: 68px; left: 49px; width: 330px; }
  .team-list { list-style: none; margin-top: 12px; }
  .team-list li { position: relative; padding-left: 25px; font-size: 19.4px; line-height: 44.7px; }
  .team-list li::before { content: ""; position: absolute; left: 4px; top: 18px; width: 9px; height: 9px;
    border-radius: 50%; background: var(--ink); }

  .provide { position: absolute; top: 481px; left: 49px; width: 340px; }
  .provide-list { list-style: none; margin-top: 19px; }
  .provide-list li { position: relative; padding-left: 27px; font-size: 18px; line-height: 28.6px; }
  .provide-list li::before { content: ""; position: absolute; left: 3px; top: 12px; width: 5px; height: 5px;
    border-radius: 50%; background: var(--ink); }
</style>
</head>
<body>
<main class="brochure">
  <svg class="backdrop" viewBox="0 0 900 695" preserveAspectRatio="none" aria-hidden="true">
    <polygon points="0,0 300,0 300,290 0,212" fill="var(--gray-light)"/>
    <polygon points="0,224 300,300 300,318 0,242" fill="var(--band-black)"/>
    <rect x="300" y="0" width="300" height="695" fill="var(--gray-dark)"/>
    <polygon points="600,292 900,216 900,226 600,302" fill="var(--gray-mid)"/>
    <polygon points="600,314 900,234 900,252 600,330" fill="var(--band-black)"/>
    <polygon points="600,342 900,262 900,695 600,695" fill="var(--gray-light)"/>
  </svg>

  <div class="backdrop" role="img" aria-label="Faint virus particle decoration on the grey cover area" style="clip-path: polygon(0 0, 400px 0, 400px 386px, 0 282px);"></div>

  <section class="panel panel--about">
    <header class="cover-title">
      <h1 class="cover-title__main">Covid-19</h1>
      <p class="cover-title__sub">Pre Screening<br>and Temperature<br>Monitoring</p>
    </header>

    <div class="about">
      <h2 class="section-heading">ABOUT US</h2>
      <p class="body-copy">Lorem Ipsum is simply dummy text of the printing and typesetting industry. Lorem Ipsum has been the industry’s standard dummy text ever since the 1500s, when an unknown printer took a galley of type and scrambled it to make a type specimen book. It has survived not only five centuries, but also the leap into electronic typesetting, remaining essentially unchanged. It was popularised in the 1960s with the release of Tessaret sheets containing Lorem Ipsum passages, and more recently with desktop publishing software like Orvel LayoutKit including versions of Lorem Ipsum.</p>
    </div>

    <div class="dots" aria-hidden="true">
      <svg class="dot" viewBox="0 0 78 80"><circle cx="39" cy="43" r="36" fill="var(--gray-dark)"/><circle cx="39" cy="37" r="36" fill="var(--band-black)"/></svg>
      <svg class="dot" viewBox="0 0 78 80"><circle cx="39" cy="43" r="36" fill="var(--gray-dark)"/><circle cx="39" cy="37" r="36" fill="var(--band-black)"/></svg>
      <svg class="dot" viewBox="0 0 78 80"><circle cx="39" cy="43" r="36" fill="var(--gray-dark)"/><circle cx="39" cy="37" r="36" fill="var(--band-black)"/></svg>
    </div>
  </section>

  <section class="panel panel--services">
    <p class="services-tagline">Trained and Certified<br>Professionals</p>
    <div class="services">
      <h2 class="section-heading">OUR CARE SERVICES</h2>
      <p class="body-copy">Lorem Ipsum is simply dummy text of the printing and typesetting industry. Lorem Ipsum has been the industry’s standard dummy text ever since the 1500s, when an unknown printer took a galley of type and scrambled it to make a type specimen book. It has survived not only five centuries, but also the leap into electronic typesetting, remaining essentially unchanged. It was popularised in the 1960s with the release of Tessaret sheets containing Lorem Ipsum passages, and more recently with desktop publishing software like Orvel LayoutKit including versions of Lorem Ipsum.</p>
      <p class="body-copy">There are many variations of passages of Lorem Ipsum available, but the majority have suffered alteration in some form, by injected humour, or randomised words which don’t look even slightly believable. If you are going to use a passage of Lorem Ipsum, you need to be sure there isn’t anything embarrassing hidden in the middle of text. All the Lorem Ipsum generators on the Internet tend to repeat predefined chunks as necessary, making this the first true generator on the Internet.</p>
    </div>
  </section>

  <section class="panel panel--team">
    <div class="team">
      <h2 class="section-heading">OUR MEDICAL TEAM:</h2>
      <ul class="team-list">
        <li>Basic First Aid</li>
        <li>Covid-19 Pre Screening</li>
        <li>Temperature Monitoring</li>
      </ul>
    </div>

    <div class="provide">
      <h2 class="section-heading">WE PROVIDE</h2>
      <ul class="provide-list">
        <li>Special Events</li>
        <li>Large Gatherings Businesses</li>
        <li>Sporting Events</li>
        <li>Carnivals</li>
        <li>Festivals</li>
        <li>Craft Shows</li>
        <li>Warehouses</li>
        <li>Churches</li>
        <li>Manufacturing Facilities</li>
        <li>Industrial Buildings</li>
        <li>Large Construction Sites</li>
        <li>Multi Occupancy Officer Buildings</li>
      </ul>
    </div>
  </section>
</main>
</body>
</html>
```